Book Cover - Life Lessons Book

I have written a book for my sons who are graduating high school and college. Working title is "Chart Your Compass.....38 Lessons Learned at Home" I am looking for the book to appeal to young adults and parents who would want to give this book to them. It is a 125 page book that will be hardback and paperback - probably 5x8 or 6x9.
Updates

Reason: Altered some of the design elements based on the first submissions received. Would really like to have designs by Monday, May 15, 2016 but could not force a 2 day extension.

Target Market(s)

Young adults -- graduates, 20-3- year olds. And, parents would would give a book to their kids

Industry/Entity Type

Book Publisher

Font styles to use
Serif

Requirements
Must have
• Great design. It is a book cover so needs to catch the attention.
Nice to have
• I am open to more animated/playful/modern look or a more traditional look. Just would like to appeal to young adults and parents.
Should not have
• Anything in poor taste

```html
<!DOCTYPE html>
<html lang="en">
<head>
<meta charset="utf-8">
<title>Chart Your Compass — 38 Lessons Learned at Home</title>
<link rel="stylesheet" href="https://fonts.googleapis.com/css2?family=Bebas+Neue&family=Black+Ops+One&family=Cabin+Sketch:wght@700&display=swap">
<style>
  :root {
    --page: #ffffff;
    --sky-top: #1c2a3a;
    --sky-mid: #2f4f78;
    --sky-low: #4f86c4;
    --grass: #1f7f22;
    --road: #7a7a76;
    --road-deep: #5d5d5a;
    --sign-blue: #0b4ba0;
    --sign-blue-deep: #08397e;
    --sign-white: #ffffff;
    --paint-yellow: #f2b91c;
    --chalk: #f4f4f0;
  }
  * { box-sizing: border-box; margin: 0; padding: 0; }
  html, body {
    width: 1016px; height: 1200px; overflow: hidden;
    background: var(--page);
  }
  .cover {
    position: absolute; left: 178px; top: 40px;
    width: 660px; height: 1120px; overflow: hidden;
    font-family: "Bebas Neue", "Arial Narrow", sans-serif;
  }
  .cover__art {
    position: absolute; inset: 0;
    background: linear-gradient(180deg,
      var(--sky-top) 0%, var(--sky-mid) 36%, var(--sky-low) 58%,
      var(--grass) 60%, var(--grass) 66%,
      var(--road) 72%, var(--road-deep) 100%);
  }
  .author-name {
    position: absolute; top: 38px; left: 0; width: 660px;
    text-align: center; color: var(--sign-white);
    font-size: 62px; letter-spacing: 1px; line-height: 1;
  }
  .sign {
    position: absolute; left: 44px; top: 178px;
    width: 566px; height: 556px;
    background: var(--sign-white); padding: 12px;
  }
  .sign__panel {
    width: 100%; height: 100%;
    background: linear-gradient(180deg, var(--sign-blue-deep), var(--sign-blue) 40%);
    color: var(--sign-white);
    display: flex; flex-direction: column; align-items: center; justify-content: center;
    gap: 4px;
  }
  .sign__row { display: flex; align-items: center; justify-content: center; gap: 18px; line-height: .9; }
  .sign__word { font-weight: 400; }
  .sign__word--big { font-size: 176px; letter-spacing: 2px; }
  .sign__word--mid { font-size: 150px; letter-spacing: 6px; }
  .sign__word--low { font-size: 132px; letter-spacing: 4px; }
  .sign__arrow { width: 50px; height: 110px; }
  .sign__turn { width: 80px; height: 80px; }
  .tagline { position: absolute; line-height: 1; white-space: nowrap; }
  .tagline--count {
    left: 110px; top: 760px; font-family: "Cabin Sketch", cursive;
    font-size: 78px; color: var(--chalk);
  }
  .tagline--lessons {
    left: 66px; top: 850px; font-family: "Black Ops One", "Impact", sans-serif;
    font-size: 104px; color: var(--paint-yellow); letter-spacing: 2px;
  }
  .tagline--learned {
    left: 74px; top: 975px; font-family: "Black Ops One", "Impact", sans-serif;
    font-size: 50px; color: var(--paint-yellow);
  }
  .tagline--home {
    left: 420px; top: 1020px; font-family: "Cabin Sketch", cursive;
    font-size: 80px; color: var(--chalk);
  }
</style>
</head>
<body>
  <main class="cover">
    <div class="cover__art" role="img" aria-label="Illustration: night sky with a yellow moon, green fields and an asphalt road leading to the horizon"></div>
    <p class="author-name">Authors Name</p>

    <section class="sign" aria-label="Title">
      <div class="sign__panel">
        <div class="sign__row">
          <svg class="sign__arrow" viewBox="0 0 50 110" aria-hidden="true"><path d="M19 0h12v78h17L25 110 2 78h17z" fill="#fff"/></svg>
          <h1 class="sign__word sign__word--big">Chart</h1>
          <svg class="sign__arrow" viewBox="0 0 50 110" aria-hidden="true"><path d="M19 110h12V32h17L25 0 2 32h17z" fill="#fff"/></svg>
        </div>
        <div class="sign__row">
          <svg class="sign__turn" viewBox="0 0 80 80" aria-hidden="true"><path d="M60 80V30H28v14L0 22 28 0v14h46v66z" fill="#fff"/></svg>
          <span class="sign__word sign__word--mid">Your</span>
          <svg class="sign__turn" viewBox="0 0 80 80" aria-hidden="true"><path d="M20 80V30h32v14l28-22L52 0v14H6v66z" fill="#fff"/></svg>
        </div>
        <div class="sign__row">
          <span class="sign__word sign__word--low">Compass</span>
        </div>
      </div>
    </section>

    <p class="tagline tagline--count">38</p>
    <p class="tagline tagline--lessons">LESSONS</p>
    <p class="tagline tagline--learned">LEARNED AT</p>
    <p class="tagline tagline--home">HOME</p>
  </main>
</body>
</html>
```